Communication and Marketing agency needs a new presentation card

We are a group of communication and marketing agencies specialized in companies that are in the logistics and industrial sector. The head agency is TELVANO Grupo and the group consists of 4 agencies: TELVANO Media, TELVANO Digital, TELVANO Research and EnlazaPorImagen. We hace 4 offices in Spain (Madrid, Barcelona, Valencia and Murcia). We are looking for a clean and attractive design that transmits our experience, brand presence in the market and knowledge to those who receive the card.It has to maintain the colors of the logo that is attached.
Target Market(s)
logistics and industrial sector
Marketing department
Clean and attractive design

```html
<!DOCTYPE html>
<html lang="en">
<head>
<meta charset="utf-8">
<title>TELVANO Grupo – Business Card</title>
<link rel="stylesheet" href="https://fonts.googleapis.com/css2?family=Tenor+Sans&display=swap">
<style>
  :root {
    --backdrop: #6e7b8c;
    --card: #ffffff;
    --brand-red: #b31b27;
    --charcoal: #2e2926;
    --ink: #3a3a3a;
    --rule: #555555;
    --font-text: "Tenor Sans", "Optima", sans-serif;
  }
  * { box-sizing: border-box; margin: 0; padding: 0; }
  html, body {
    width: 1200px; height: 1200px; overflow: hidden;
    background: var(--backdrop);
    font-family: var(--font-text);
  }
  .canvas { position: relative; width: 1200px; height: 1200px; }
  .card {
    position: absolute; left: 120px; width: 960px; height: 548px;
    background: var(--card); overflow: hidden;
  }
  .card--back  { top: 40px; }
  .card--front { top: 612px; }
  .swoosh { position: absolute; inset: 0; width: 100%; height: 100%; }

  /* Back side: agency names */
  .agency-list {
    position: absolute; right: 50px; top: 220px;
    display: grid; grid-template-columns: auto auto;
    column-gap: 36px; row-gap: 34px; align-items: end;
  }
  .agency { font-size: 28px; letter-spacing: 1px; white-space: nowrap; }
  .agency--gray { color: var(--ink); }
  .agency--red  { color: var(--brand-red); }

  /* Front side */
  .brand-name {
    position: absolute; left: 64px; top: 70px;
    font-size: 66px; letter-spacing: 2px; color: var(--brand-red);
  }
  .holder { position: absolute; left: 64px; top: 360px; }
  .holder-name { font-size: 26px; color: var(--brand-red); letter-spacing: 1px; }
  .holder-role { font-size: 24px; color: var(--ink); margin-top: 4px; }
  .contact-rule {
    position: absolute; left: 300px; top: 428px; width: 450px; height: 1px;
    background: var(--rule);
  }
  .contact {
    position: absolute; left: 64px; top: 440px;
    display: flex; gap: 26px; font-size: 22px; line-height: 1.35; color: var(--ink);
    letter-spacing: 0.5px;
  }
</style>
</head>
<body>
<main class="canvas">

  <section class="card card--back" aria-label="Card back">
    <svg class="swoosh" viewBox="0 0 960 548" preserveAspectRatio="none" aria-hidden="true">
      <path fill="var(--charcoal)" d="M0 70 C50 80 110 170 190 240 C270 310 330 420 370 548 L0 548 Z"/>
      <path fill="var(--brand-red)" d="M62 0 C100 100 160 190 240 250 C320 310 370 420 400 548 L362 548 C330 430 275 330 200 265 C120 200 70 110 30 0 Z"/>
      <path fill="var(--card)" d="M66 0 C100 90 150 170 220 225 C180 200 120 130 82 0 Z"/>
    </svg>
    <div class="agency-list">
      <span class="agency agency--gray">TELVANO Digital</span>
      <span class="agency agency--gray">TELVANO Research</span>
      <span class="agency agency--red">TELVANO Media</span>
      <span class="agency agency--red">EnlazaPorImagen</span>
    </div>
  </section>

  <section class="card card--front" aria-label="Card front">
    <svg class="swoosh" viewBox="0 0 960 548" preserveAspectRatio="none" aria-hidden="true">
      <path fill="var(--charcoal)" d="M830 0 C880 120 895 210 855 305 C815 395 810 470 830 548 L960 548 L960 0 Z"/>
      <path fill="var(--brand-red)" d="M780 0 C845 120 865 215 820 315 C785 400 785 480 800 548 L835 548 C818 470 830 390 866 300 C905 205 885 110 838 0 Z"/>
      <path fill="var(--card)" d="M812 0 C858 110 872 200 840 290 C860 200 845 110 824 0 Z"/>
    </svg>
    <div class="brand-name">TELVANO Grupo</div>
    <div class="holder">
      <div class="holder-name">LUCÍA MARTÍN</div>
      <div class="holder-role">Director</div>
    </div>
    <div class="contact-rule"></div>
    <div class="contact">
      <div class="contact-lines">
        <div>+34 600 482 915</div>
        <div>lucia@telvanogrupo.es</div>
        <div>www.telvanogrupo.es</div>
      </div>
      <div class="contact-address">
        <div>Dummy Street</div>
        <div>Dummy City, Dummy Country</div>
      </div>
    </div>
  </section>

</main>
</body>
</html>
```